General Contractor Company introduction and presentation

i need a company presentation design for a construction company called K3 Building Corp. we build brand ground up affordable apartment building as well Remodeling of apartment units and commercial buildings.
company was established in June 2020.

```html
<!DOCTYPE html>
<html lang="en">
<head>
<meta charset="utf-8">
<title>K3 Building Corp. – Company Presentation</title>
<link href="https://fonts.googleapis.com/css2?family=Poppins:wght@300;400;500;600;700;800&display=swap" rel="stylesheet">
<style>
:root{
  --green:#6fdc4f;
  --green-soft:#d9f5cf;
  --green-pale:#e6f8de;
  --ink:#111111;
  --grey-text:#9a9a9a;
  --board:#707070;
  --sidebar:#f1f1f1;
  --sidebar-foot:#e5e5e5;
  --dark:#0f0f0f;
  --dark-2:#262626;
  --white:#ffffff;
}
*{box-sizing:border-box;margin:0;padding:0}
html,body{width:825px;height:1200px;overflow:hidden}
body{background:var(--board);font-family:"Poppins",sans-serif;color:var(--ink);position:relative}
.slide{position:absolute;width:391px;height:220px;background:var(--white);overflow:hidden;box-shadow:0 2px 6px rgba(0,0,0,.35)}
.col-l{left:15px}.col-r{left:419px}
.row-1{top:22px}.row-2{top:256px}.row-3{top:490px}.row-4{top:724px}.row-5{top:958px}
.abs{position:absolute}

/* brand mark */
.brand{display:flex;flex-direction:column;align-items:center;gap:4px}
.brand-square{width:14px;height:14px;background:var(--green)}
.brand-name{font-weight:700;font-size:4.6px;letter-spacing:1.4px;text-align:center;line-height:1.35;color:var(--ink)}

/* sidebar template */
.sidebar{position:absolute;left:0;top:0;width:60px;height:220px;background:var(--sidebar)}
.sidebar .brand{position:absolute;top:30px;left:0;width:60px}
.sidebar-foot{position:absolute;left:0;bottom:0;width:60px;height:49px;background:var(--sidebar-foot);padding:12px 0 0 7px;font-size:3px;line-height:4.3px;color:#8a8a8a}
.sidebar-foot b{color:var(--ink);font-weight:700}

.address-block{font-size:3.5px;line-height:5.3px;color:#a8a8a8}
.address-block b{color:var(--ink);font-weight:700}

/* titles */
.title{position:absolute;top:47px;font-weight:700;font-size:10px;letter-spacing:1.2px;display:flex;gap:3px;align-items:center;white-space:nowrap}
.title .hl{background:var(--green);padding:1px 4px}
.title.center{left:60px;right:0;justify-content:center}

.placeholder{position:absolute}

/* contact */
.contact{font-size:3.6px;line-height:8px;color:#555}
.contact .phone{font-weight:700;font-size:5.4px;color:var(--ink)}
.contact-line{display:flex;align-items:center;gap:4px}
.contact svg{width:5px;height:5px;flex:none}

/* completed projects */
.big-num{font-weight:800;font-size:46px;line-height:1;letter-spacing:-2px;display:flex;align-items:flex-end}
.big-num span{font-size:10px;font-weight:600;letter-spacing:.4px;margin:0 0 3px 2px}
.proj-addr{font-size:5.6px;font-weight:600}
.dates{display:flex;gap:12px;font-size:3.4px;color:#444}
.dates small{display:block;font-size:2.4px;color:#999;font-weight:600}

/* pre-construction */
.unit-num{position:absolute;font-weight:700;text-align:center;transform:translateX(-50%);line-height:1;font-size:22px}
.unit-num small{display:block;font-size:4.2px;font-weight:600;margin-top:3px}
.house-addr{position:absolute;font-size:4.6px;font-weight:600;text-align:center;line-height:6.6px;transform:translateX(-50%);width:70px}
.house-art{position:absolute;background:linear-gradient(180deg,#e2f7d9 0%,var(--green-soft) 100%)}

/* skills */
.skill{position:absolute;font-size:8.4px;font-weight:600;white-space:nowrap}
.skill-plain{position:absolute;font-size:8.4px;font-weight:400;white-space:nowrap}
</style>
</head>
<body>

<!-- Cover with photo -->
<section class="slide col-l row-1">
  <div class="placeholder" role="img" aria-label="Photo of a smiling family standing in front of their new suburban home" style="inset:0;background:linear-gradient(160deg,#6d7a58 0%,#8e8f86 40%,#5c6447 75%,#3f4632 100%)"></div>
  <div class="abs" style="left:0;top:122px;width:140px;height:83px;background:var(--white);border-radius:0 8px 8px 0"></div>
  <div class="abs" style="left:0;top:121px;width:98px;height:12px;background:var(--white);border-radius:0 8px 0 0"></div>
  <div class="brand abs" style="left:6px;top:142px;width:42px">
    <div class="brand-square"></div>
    <div class="brand-name">K3 BUILDING<br>CORP</div>
  </div>
  <div class="address-block abs" style="left:72px;top:165px">K3 Building Corp.<br>2400 Harbor Way, Suite 210<br>Fairview, CA 90010<br><b>555-014-1222</b><br>LICENSE NO. 0042817</div>
  <div class="contact abs" style="left:287px;top:130px;width:104px;height:36px;background:var(--white);border-radius:6px 0 0 6px;padding:3px 0 0 7px">
    <div class="contact-line phone"><svg viewBox="0 0 10 10"><path d="M2 1l2 2-1 1.5q1 2 3 3L7.5 6.5l2 2L8 10Q1 9 0 2z" fill="#111"/></svg>555-018-2050</div>
    <div class="contact-line"><svg viewBox="0 0 10 10"><rect x="0" y="2" width="10" height="6" fill="#111"/><path d="M0 2l5 3 5-3" stroke="#fff" fill="none"/></svg>dana@k3building.com</div>
    <div class="contact-line"><svg viewBox="0 0 10 10"><path d="M5 10L1.5 5A3.5 3.5 0 1 1 8.5 5z" fill="#111"/><circle cx="5" cy="3.6" r="1.3" fill="#fff"/></svg>Fairview, CA 90010</div>
  </div>
  <div class="contact abs" style="left:287px;top:168px;width:104px;height:36px;background:var(--white);border-radius:6px 0 0 6px;padding:3px 0 0 7px">
    <div class="contact-line phone"><svg viewBox="0 0 10 10"><path d="M2 1l2 2-1 1.5q1 2 3 3L7.5 6.5l2 2L8 10Q1 9 0 2z" fill="#111"/></svg>555-014-1222</div>
    <div class="contact-line"><svg viewBox="0 0 10 10"><rect x="0" y="2" width="10" height="6" fill="#111"/><path d="M0 2l5 3 5-3" stroke="#fff" fill="none"/></svg>joel@k3building.com</div>
    <div class="contact-line"><svg viewBox="0 0 10 10"><path d="M5 10L1.5 5A3.5 3.5 0 1 1 8.5 5z" fill="#111"/><circle cx="5" cy="3.6" r="1.3" fill="#fff"/></svg>Fairview, CA 90010</div>
  </div>
  <div class="abs" style="left:0;right:0;top:207px;height:1.5px;background:var(--green)"></div>
  <div class="abs" style="left:0;right:0;top:209px;bottom:0;background:#2a2d22"></div>
</section>

<!-- Cover with drawing -->
<section class="slide col-r row-1">
  <div class="placeholder" role="img" aria-label="Architectural wireframe drawing of a multi-storey building" style="left:170px;top:0;right:0;bottom:0;background:linear-gradient(120deg,#ffffff 0%,#f1f1f1 45%,#e4e4e4 100%)"></div>
  <div class="brand abs" style="left:15px;top:18px;align-items:flex-start">
    <div class="brand-square" style="width:18px;height:18px"></div>
    <div class="brand-name" style="text-align:left;font-size:5px">K3 BUILDING<br>CORP</div>
  </div>
  <div class="address-block abs" style="left:18px;top:78px">K3 Building Corp.<br>2400 Harbor Way, Suite 210<br>Fairview, CA 90010<br><b>555-014-1222</b><br>LICENSE NO. 0042817</div>
  <div class="abs" style="left:0;top:176px;width:194px;height:33px;background:var(--dark-2);border-radius:0 6px 6px 0"></div>
  <div class="abs" style="left:0;top:176px;width:102px;height:33px;background:var(--dark)"></div>
  <div class="contact abs" style="left:16px;top:180px;color:#ccc">
    <div class="contact-line phone" style="color:var(--green)"><svg viewBox="0 0 10 10"><path d="M2 1l2 2-1 1.5q1 2 3 3L7.5 6.5l2 2L8 10Q1 9 0 2z" fill="#888"/></svg>555-018-2050</div>
    <div class="contact-line"><svg viewBox="0 0 10 10"><rect x="0" y="2" width="10" height="6" fill="#888"/></svg>dana@k3building.com</div>
    <div class="contact-line"><svg viewBox="0 0 10 10"><path d="M5 10L1.5 5A3.5 3.5 0 1 1 8.5 5z" fill="#888"/></svg>Fairview, CA 90010</div>
  </div>
  <div class="contact abs" style="left:110px;top:180px;color:#ccc">
    <div class="contact-line phone" style="color:var(--green)"><svg viewBox="0 0 10 10"><path d="M2 1l2 2-1 1.5q1 2 3 3L7.5 6.5l2 2L8 10Q1 9 0 2z" fill="#888"/></svg>555-014-1222</div>
    <div class="contact-line"><svg viewBox="0 0 10 10"><rect x="0" y="2" width="10" height="6" fill="#888"/></svg>joel@k3building.com</div>
    <div class="contact-line"><svg viewBox="0 0 10 10"><path d="M5 10L1.5 5A3.5 3.5 0 1 1 8.5 5z" fill="#888"/></svg>Fairview, CA 90010</div>
  </div>
</section>

<!-- Completed projects -->
<section class="slide col-l row-2">
  <aside class="sidebar">
    <div class="brand"><div class="brand-square"></div><div class="brand-name">K3 BUILDING<br>CORP</div></div>
    <div class="sidebar-foot">K3 Building Corp.<br>2400 Harbor Way, Ste 210<br>Fairview, CA 90010<br><b>555-014-1222</b><br>LICENSE NO. 0042817</div>
  </aside>
  <h2 class="title center"><span class="hl">COMPLETED</span>PROJECTS</h2>
  <svg class="abs" style="left:160px;top:76px" width="112" height="130" viewBox="0 0 112 130">
    <path d="M56 130 C48 112 6 94 6 50 A50 50 0 1 1 106 50 C106 94 64 112 56 130Z" fill="var(--green-pale)"/>
  </svg>
  <div class="placeholder" role="img" aria-label="Illustration of a two-storey family house on a lawn" style="left:184px;top:95px;width:64px;height:64px;border-radius:50%;background:radial-gradient(circle at 50% 60%,#c9cfc4 0%,#8fd676 60%,var(--green) 100%)"></div>
  <div class="abs" style="left:154px;top:118px;width:26px;height:.7px;background:#333"></div>
  <div class="abs" style="left:251px;top:118px;width:26px;height:.7px;background:#333"></div>
  <div class="big-num abs" style="left:74px;top:92px">17<span>UNITS</span></div>
  <div class="proj-addr abs" style="left:81px;top:152px">418 Maple Street, Fairview</div>
  <div class="dates abs" style="left:81px;top:162px"><div><small>START DATE</small>10/01/2021</div><div><small>END DATE</small>07/12/2023</div></div>
  <div class="big-num abs" style="left:280px;top:92px">18<span>UNITS</span></div>
  <div class="proj-addr abs" style="left:286px;top:152px">422 Maple Street, Fairview</div>
  <div class="dates abs" style="left:286px;top:162px"><div><small>START DATE</small>1/01/2022</div><div><small>END DATE</small>05/29/2024</div></div>
</section>

<!-- Professional summary -->
<section class="slide col-r row-2">
  <aside class="sidebar">
    <div class="brand"><div class="brand-square"></div><div class="brand-name">K3 BUILDING<br>CORP</div></div>
    <div class="sidebar-foot">K3 Building Corp.<br>2400 Harbor Way, Ste 210<br>Fairview, CA 90010<br><b>555-014-1222</b><br>LICENSE NO. 0042817</div>
  </aside>
  <div class="placeholder" role="img" aria-label="Line drawing of residential buildings in perspective" style="left:275px;top:80px;right:0;bottom:0;background:linear-gradient(200deg,#f0f0f0 0%,#fafafa 60%,#ffffff 100%)"></div>
  <svg class="abs" style="left:120px;top:0" width="271" height="120" viewBox="0 0 271 120"><path d="M0 0 L200 110 M30 0 L271 92" stroke="#444" stroke-width=".5" fill="none"/></svg>
  <h2 class="title" style="left:72px"><span class="hl">PROFESSIONAL</span>SUMMARY</h2>
  <p class="abs" style="left:76px;top:84px;width:146px;font-size:6.7px;line-height:9.4px;color:#555;font-weight:300">Committed and motivated general contractor company with almost a decade of experience in the residential, and commercial construction and retail sectors. Proven track of analyzing construction plans and proposals and identifying affordable sources of material and labor. Highly knowledgeable about the fundamental construction principles, customer service, project management.</p>
</section>

<!-- Under construction -->
<section class="slide col-l row-3">
  <aside class="sidebar">
    <div class="brand"><div class="brand-square"></div><div class="brand-name">K3 BUILDING<br>CORP</div></div>
    <div class="sidebar-foot">K3 Building Corp.<br>2400 Harbor Way, Ste 210<br>Fairview, CA 90010<br><b>555-014-1222</b><br>LICENSE NO. 0042817</div>
  </aside>
  <h2 class="title center"><span class="hl">UNDER</span>CONSTRUCTION</h2>
  <div class="placeholder" role="img" aria-label="Illustration of two tower cranes over faint building sketches" style="left:105px;top:66px;width:236px;height:154px;background:linear-gradient(180deg,#fafafa 0%,#f0f0f0 100%)"></div>
  <div class="abs" style="left:190px;top:103px;width:49px;height:34px;background:var(--green-soft);display:flex;align-items:center;justify-content:center;font-weight:700;font-size:31px;letter-spacing:-1px">18</div>
  <div class="abs" style="left:150px;width:130px;top:141px;text-align:center;font-size:10.5px;font-weight:500">UNITS</div>
  <div class="abs" style="left:150px;width:130px;top:157px;text-align:center;font-size:5.6px;font-weight:600">705 Cedar Ave, Fairview, CA</div>
  <div class="abs" style="left:150px;width:130px;top:167px;text-align:center;font-size:3.4px;color:#444"><span style="display:block;font-size:2.4px;color:#999;font-weight:600">START DATE</span>10/15/2024</div>
</section>

<!-- Pre-construction -->
<section class="slide col-r row-3">
  <aside class="sidebar">
    <div class="brand"><div class="brand-square"></div><div class="brand-name">K3 BUILDING<br>CORP</div></div>
    <div class="sidebar-foot">K3 Building Corp.<br>2400 Harbor Way, Ste 210<br>Fairview, CA 90010<br><b>555-014-1222</b><br>LICENSE NO. 0042817</div>
  </aside>
  <h2 class="title" style="left:72px"><span class="hl">PRE</span>- CONSTRUCTION</h2>

  <div class="house-art" role="img" aria-label="Illustration of a pale green apartment building, 52 units" style="left:74px;top:139px;width:66px;height:81px"></div>
  <div class="house-art" role="img" aria-label="Illustration of a pale green apartment building, 72 units" style="left:147px;top:119px;width:66px;height:101px"></div>
  <div class="house-art" role="img" aria-label="Illustration of a pale green apartment building, 72 units" style="left:222px;top:119px;width:66px;height:101px"></div>
  <div class="house-art" role="img" aria-label="Illustration of a pale green apartment building, 120 units" style="left:296px;top:86px;width:66px;height:134px"></div>

  <svg class="abs" style="left:0;top:0" width="391" height="220" viewBox="0 0 391 220">
    <g fill="none" stroke="#444" stroke-width=".8">
      <path d="M107 194 L105 190.5 A2 2 0 1 1 109 190.5Z"/>
      <path d="M180 194 L178 190.5 A2 2 0 1 1 182 190.5Z"/>
      <path d="M255 194 L253 190.5 A2 2 0 1 1 257 190.5Z"/>
      <path d="M329 194 L327 190.5 A2 2 0 1 1 331 190.5Z"/>
    </g>
  </svg>

  <div class="unit-num" style="left:107px;top:106px">52<small>Units</small></div>
  <div class="unit-num" style="left:180px;top:86px">72<small>Units</small></div>
  <div class="unit-num" style="left:255px;top:86px">72<small>Units</small></div>
  <div class="unit-num" style="left:329px;top:53px">120<small>Units</small></div>
  <div class="house-addr" style="left:107px;top:197px">1180 Birch St,<br>Lakeview, CA</div>
  <div class="house-addr" style="left:180px;top:197px">2204 Elm Ave.<br>Lakeview, CA</div>
  <div class="house-addr" style="left:255px;top:197px">3310 Summit Blvd,<br>Westdale, CA</div>
  <div class="house-addr" style="left:329px;top:197px">916 Oak Ridge<br>Ave., Fairview, CA</div>
</section>

<!-- Skills tree -->
<section class="slide col-l row-4">
  <aside class="sidebar">
    <div class="brand"><div class="brand-square"></div><div class="brand-name">K3 BUILDING<br>CORP</div></div>
    <div class="sidebar-foot">K3 Building Corp.<br>2400 Harbor Way, Ste 210<br>Fairview, CA 90010<br><b>555-014-1222</b><br>LICENSE NO. 0042817</div>
  </aside>
  <h2 class="title" style="left:150px;right:-7px;justify-content:center">SKILLS</h2>
  <div class="placeholder" role="img" aria-label="Illustration of a green house and paint roller growing from a plant stem" style="left:196px;top:72px;width:80px;height:148px;background:linear-gradient(180deg,#7de35f 0%,#b5eea0 55%,#d9f5cf 100%);border-radius:4px 4px 0 0"></div>
  <svg class="abs" style="left:0;top:0" width="391" height="220" viewBox="0 0 391 220">
    <g fill="var(--green-soft)" stroke="#fff" stroke-width="1">
      <circle cx="189" cy="145" r="9"/><circle cx="173" cy="173" r="9"/><circle cx="260" cy="145" r="9"/><circle cx="276" cy="173" r="9"/>
    </g>
    <g fill="#444">
      <rect x="185" y="141" width="8" height="8" rx="1"/><rect x="169" y="169" width="8" height="8"/>
      <path d="M256 147 L260 142 L264 147 V150 H256Z"/><circle cx="276" cy="171" r="2.5"/><path d="M271.5 178 A4.5 4 0 0 1 280.5 178Z"/>
    </g>
  </svg>
  <div class="skill" style="right:216px;top:138px">Bidding and estimating</div>
  <div class="skill" style="right:231px;top:166px">Project management</div>
  <div class="skill" style="left:275px;top:138px">Construction sales</div>
  <div class="skill" style="left:292px;top:166px">Customer service</div>
</section>

<!-- Skills diagram -->
<section class="slide col-r row-4">
  <aside class="sidebar">
    <div class="brand"><div class="brand-square"></div><div class="brand-name">K3 BUILDING<br>CORP</div></div>
    <div class="sidebar-foot">K3 Building Corp.<br>2400 Harbor Way, Ste 210<br>Fairview, CA 90010<br><b>555-014-1222</b><br>LICENSE NO. 0042817</div>
  </aside>
  <svg class="abs" style="left:0;top:0" width="391" height="220" viewBox="0 0 391 220">
    <path d="M120 54 A69 69 0 0 1 120 192Z" fill="var(--green-pale)"/>
    <circle cx="120" cy="123" r="44" fill="#fff" stroke="var(--green)" stroke-width="1"/>
    <g stroke="#666" stroke-width=".5" stroke-dasharray="1 1">
      <line x1="166" y1="73" x2="216" y2="73"/><line x1="188" y1="108" x2="238" y2="108"/>
      <line x1="184" y1="149" x2="235" y2="149"/><line x1="159" y1="180" x2="200" y2="180"/>
    </g>
    <g fill="#fff" stroke="#111" stroke-width="1.1">
      <circle cx="166" cy="73" r="2.4"/><circle cx="188" cy="108" r="2.4"/><circle cx="184" cy="149" r="2.4"/><circle cx="159" cy="180" r="2.4"/>
    </g>
    <g fill="var(--green)">
      <rect x="219" y="63" width="20" height="20" transform="rotate(45 229 73)"/>
      <rect x="241" y="98" width="20" height="20" transform="rotate(45 251 108)"/>
      <rect x="238" y="139" width="20" height="20" transform="rotate(45 248 149)"/>
      <rect x="203" y="170" width="20" height="20" transform="rotate(45 213 180)"/>
    </g>
    <g fill="#fff">
      <rect x="225" y="69" width="8" height="8" rx="1"/><rect x="247" y="104" width="8" height="8"/>
      <path d="M244 151 L248 146 L252 151 V154 H244Z"/><circle cx="213" cy="178" r="2.5"/><path d="M208.5 185 A4.5 4 0 0 1 217.5 185Z"/>
    </g>
  </svg>
  <div class="abs" style="left:76px;width:88px;top:116px;text-align:center;font-weight:700;font-size:10px;letter-spacing:1px">SKILLS</div>
  <div class="skill-plain" style="left:248px;top:68px">Bidding and estimating</div>
  <div class="skill-plain" style="left:270px;top:103px">Project management</div>
  <div class="skill-plain" style="left:267px;top:144px">Construction sales</div>
  <div class="skill-plain" style="left:233px;top:175px">Customer service</div>
</section>

<!-- Certification -->
<section class="slide col-l row-5">
  <aside class="sidebar">
    <div class="brand"><div class="brand-square"></div><div class="brand-name">K3 BUILDING<br>CORP</div></div>
    <div class="sidebar-foot">K3 Building Corp.<br>2400 Harbor Way, Ste 210<br>Fairview, CA 90010<br><b>555-014-1222</b><br>LICENSE NO. 0042817</div>
  </aside>
  <h2 class="title" style="left:129px">CERTIFICATION</h2>
  <div class="abs" style="left:114px;top:104px;width:112px;height:24px;background:#1f4e8c;border-radius:3px"></div>
  <div class="abs" style="left:100px;width:142px;top:137px;text-align:center;font-size:8px;line-height:11.5px">State Contractors Licensing<br>Board <b>0042817</b></div>
  <svg class="abs" style="left:274px;top:84px" width="76" height="76" viewBox="0 0 76 76">
    <circle cx="38" cy="38" r="37" fill="var(--green)"/>
    <circle cx="38" cy="38" r="22" fill="#fff"/>
    <path d="M28 39 L35 46 L49 31" stroke="#555" stroke-width="6" fill="none" stroke-linecap="round" stroke-linejoin="round"/>
  </svg>
</section>

<!-- Closing -->
<section class="slide col-r row-5">
  <div class="brand abs" style="left:0;right:0;top:72px;gap:10px">
    <div class="brand-square" style="width:26px;height:26px"></div>
    <div class="brand-name" style="font-size:10.5px;letter-spacing:2.6px;line-height:12.5px">K3 BUILDING<br>CORP</div>
  </div>
</section>

</body>
</html>
```